TRV Business Card

Business card design for a handyman company. Want to portray a professional image and stay away from the "Mom & Pops" image that is normally associated with handyman companies.

Business

```html
<!DOCTYPE html>
<html lang="en">
<head>
<meta charset="utf-8">
<title>TRV Business Card</title>
<link rel="stylesheet" href="https://fonts.googleapis.com/css2?family=Montserrat:wght@300;400;800&display=swap">
<style>
  :root {
    --backdrop: #e9e7e4;
    --card: #ffffff;
    --navy: #0f2347;
    --navy-deep: #0a1a38;
    --accent-blue: #2f6fc8;
    --rim-grey: #c9ced6;
    --muted: #6b7280;
    --on-navy: #ffffff;
  }
  * { box-sizing: border-box; margin: 0; padding: 0; }
  html, body {
    width: 1200px; height: 867px; overflow: hidden;
    background: var(--backdrop);
    font-family: "Montserrat", Arial, sans-serif;
  }
  .business-card {
    position: absolute; left: 100px; top: 148px;
    width: 1000px; height: 571px;
    background: var(--card);
    box-shadow: 0 10px 30px rgba(0,0,0,.18);
    overflow: hidden;
  }
  .card-swoosh { position: absolute; inset: 0; width: 100%; height: 100%; }
  .brand-name {
    position: absolute; left: 62px; top: 70px;
    font-weight: 800; font-size: 120px; line-height: 1;
    letter-spacing: 4px; color: var(--navy);
  }
  .contact-block {
    position: absolute; left: 62px; top: 380px;
    font-size: 18px; font-weight: 400; color: var(--muted);
    line-height: 1.5;
  }
  .contact-address { margin-top: 22px; }
  .services-panel {
    position: absolute; left: 620px; top: 330px;
    color: var(--on-navy);
  }
  .services-title {
    font-weight: 300; font-size: 25px; line-height: 1.25;
    letter-spacing: 1.5px; text-transform: uppercase;
  }
  .services-label {
    margin-top: 24px; font-size: 17px; letter-spacing: 1px;
    text-transform: uppercase; font-weight: 400;
  }
  .services-list {
    list-style: none; margin-top: 8px;
    display: grid; grid-template-columns: 155px 185px; row-gap: 4px;
    font-size: 15px; font-weight: 400;
  }
  .services-list li::before {
    content: ""; display: inline-block; width: 10px; height: 10px;
    background: var(--on-navy); margin-right: 9px; vertical-align: 1px;
  }
</style>
</head>
<body>
  <div class="business-card">
    <svg class="card-swoosh" viewBox="0 0 1000 571" aria-hidden="true">
      <path d="M410 571 C420 310 620 165 1000 132 L1000 571 Z" fill="var(--rim-grey)"/>
      <path d="M425 571 C435 320 630 177 1000 146 L1000 571 Z" fill="var(--accent-blue)"/>
      <path d="M440 571 C450 330 640 190 1000 160 L1000 571 Z" fill="var(--navy)"/>
      <path d="M440 571 C450 330 640 190 1000 160" fill="none" stroke="var(--navy-deep)" stroke-width="3"/>
    </svg>

    <div class="brand-name">TRV</div>

    <div class="contact-block">
      <p class="contact-phone">P: (555) 014-2207</p>
      <p class="contact-fax">F: (555) 014-2281</p>
      <p class="contact-email">E: info@trvservices.example</p>
      <p class="contact-address">410 Harlow St, Millbrook, KS 00000</p>
    </div>

    <div class="services-panel">
      <h2 class="services-title">Residential &amp;<br>Commercial Services</h2>
      <p class="services-label">Potential Verbage:</p>
      <ul class="services-list">
        <li>Home Repairs</li>
        <li>Handyman Services</li>
        <li>Drain Cleaning</li>
        <li>Carpet Cleaning</li>
      </ul>
    </div>
  </div>
</body>
</html>
```